Business Card Design Project

We are VT Meridian, a recruitment company based in London. We require a new business card design in order to present our business. We work in a number of areas recruiting professional in areas such as engineering and rail. Most of our work is based in the Middle East so our cards must have a universal, professional feel.

Visit our website: http://www.vt-meridian.example.co.uk/ for more info

Industry/Entity Type

Business

Requirements
Must have
• Must be double sided

Must feature the companies logo on both sides of the card

Should incorporate the primary colours of the logo

Must be professional and contemporary, to fit in with the logo

Info: Name: Colin Prewett certRX MRQA
Senior Recruitment Consultant
Address: 7 Quarry Row Fulwell London N41QZ
T: +44 (0)203 555 0147
M: +44 (0)7700 900 318
E: cprewett@vt-meridian.example.co.uk
W www.vt-meridian.example.co.uk
Nice to have
• A modern style card

```html
<!DOCTYPE html>
<html lang="en">
<head>
<meta charset="utf-8">
<title>VT Meridian – Business Card</title>
<link rel="stylesheet" href="https://fonts.googleapis.com/css2?family=Questrial&family=Open+Sans:wght@400;700&display=swap">
<style>
  :root {
    --backdrop: #3b3b3c;
    --card-white: #f4f4f3;
    --card-grey: #6e6e6f;
    --brand-green: #17977d;
    --brand-grey: #747475;
    --band-grey: #8a8a8b;
    --text-grey: #6a6a6a;
    --text-light: #e2e2e2;
  }
  * { margin: 0; padding: 0; box-sizing: border-box; }
  html, body { width: 1200px; height: 1000px; overflow: hidden; }
  body { background: var(--backdrop); position: relative; font-family: "Questrial", "Century Gothic", sans-serif; }

  .card {
    position: absolute; width: 530px; height: 302px; border-radius: 16px; overflow: hidden;
    box-shadow: 0 6px 14px rgba(0,0,0,0.35);
  }
  .card--front { left: 165px; top: 163px; background: var(--card-white); }
  .card--back { left: 473px; top: 549px; background: var(--card-grey); }

  .brand { position: absolute; display: flex; align-items: center; gap: 14px; }
  .brand__dot { width: 62px; height: 62px; border-radius: 50%; background: var(--brand-green); flex: none; }
  .brand__name { font-family: "Questrial", "Century Gothic", sans-serif; font-size: 54px; line-height: 1; letter-spacing: -0.5px; white-space: nowrap; }
  .card--front .brand { left: 50px; top: 40px; }
  .card--front .brand__name { color: var(--brand-grey); }
  .card--back .brand { left: 50px; top: 40px; }
  .card--back .brand__name { color: #ffffff; }

  .holder { position: absolute; right: 298px; top: 171px; text-align: right; color: var(--text-grey); font-size: 13.3px; line-height: 20px; white-space: nowrap; }
  .holder__name { font-family: "Open Sans", sans-serif; font-weight: 700; font-size: 15px; letter-spacing: 0.5px; margin-bottom: 1px; color: #5f5f5f; }

  .divider { position: absolute; left: 251px; top: 154px; width: 1px; height: 92px; background: #cfcfcf; }

  .contacts { position: absolute; left: 270px; top: 164px; list-style: none; color: var(--text-grey); font-size: 13px; white-space: nowrap; }
  .contacts li { display: flex; align-items: center; height: 19.5px; }
  .contacts svg { width: 14px; height: 14px; margin-right: 14px; flex: none; }

  .band { position: absolute; left: 0; bottom: 0; height: 17px; }
  .card--front .band--grey { width: 249px; background: var(--band-grey); }
  .card--front .band--green { left: 254px; right: 0; background: var(--brand-green); }
  .card--back .band--grey { width: 205px; background: var(--band-grey); }
  .card--back .band--green { left: 208px; right: 0; background: var(--brand-green); }

  .address { position: absolute; right: 50px; top: 249px; color: var(--text-light); font-size: 13.5px; white-space: nowrap; }
</style>
</head>
<body>

<section class="card card--front" aria-label="Business card front">
  <div class="brand">
    <span class="brand__dot"></span>
    <span class="brand__name">VT Meridian</span>
  </div>

  <div class="holder">
    <p class="holder__name">COLIN PREWETT</p>
    <p>Senior Recruitment Consultant</p>
    <p>certRX MRQA</p>
  </div>

  <div class="divider"></div>

  <ul class="contacts">
    <li>
      <svg viewBox="0 0 14 14" fill="none" stroke="var(--brand-green)" stroke-width="1.2"><circle cx="7" cy="7" r="6.2"/><rect x="5" y="3.6" width="4" height="6.8" rx="0.8"/></svg>
      +44 (0)7700 900 318
    </li>
    <li>
      <svg viewBox="0 0 14 14" fill="none" stroke="var(--brand-green)" stroke-width="1.2"><circle cx="7" cy="7" r="6.2"/><path d="M4.6 4c.6 2.8 2.4 4.8 5.2 5.6l.7-1.3-1.5-.8-.7.6c-1-.5-1.8-1.3-2.2-2.3l.6-.7-.8-1.5z"/></svg>
      +44 (0)203 555 0147
    </li>
    <li>
      <svg viewBox="0 0 14 14"><circle cx="7" cy="7" r="6.8" fill="var(--brand-green)"/><rect x="3.8" y="4.8" width="6.4" height="4.4" fill="none" stroke="#fff" stroke-width="0.9"/><path d="M3.8 4.8 7 7.4l3.2-2.6" fill="none" stroke="#fff" stroke-width="0.9"/></svg>
      cprewett@vt-meridian.example.co.uk
    </li>
    <li>
      <svg viewBox="0 0 14 14" fill="none" stroke="var(--brand-green)" stroke-width="1"><circle cx="7" cy="7" r="6.2"/><ellipse cx="7" cy="7" rx="2.6" ry="6.2"/><path d="M0.8 7h12.4M2 3.8h10M2 10.2h10"/></svg>
      www.vt-meridian.example.co.uk
    </li>
  </ul>

  <div class="band band--grey"></div>
  <div class="band band--green"></div>
</section>

<section class="card card--back" aria-label="Business card back">
  <div class="brand">
    <span class="brand__dot"></span>
    <span class="brand__name">VT Meridian</span>
  </div>

  <p class="address">7 Quarry Row Fulwell London N41QZ</p>

  <div class="band band--grey"></div>
  <div class="band band--green"></div>
</section>

</body>
</html>
```